Foot and ankle surgeon requires a website design

I need a website where prospective and established patients can obtain information and then direct them to making appointments. My practice is a highly professional surgical practice specialising in surgery to the foot and ankle. My title is Mr Colin Dwyer, Podiatric Foot & Ankle Surgeon. My qualifications are: BSc MSc FACPS
The practice website will require information on: Locations, phone numbers to make appointments, general background on podiatric surgery,
I would like to include information on: my hospital appointments, surgical fellowships held, training programs undertaken, association memberships, publications written, links to useful websites
A page dedicated to common foot conditions would be useful and also a page with referral information including an online registration section that will be sent direct to the receptionist.
Examples of similar websites include:
http://www.trevorkeplinfeet.com.au/
http://www.vollardfootsurgeon.com.au/
I will provide files on logo, self photos and my personal training history etc.
Also if there is going to be a background theme I personally am associated with surfing and beach activities, it would be great if this was able to be reflected in the design.
Thank you.

```html
<!DOCTYPE html>
<html lang="en">
<head>
<meta charset="utf-8">
<title>Mr Colin Dwyer – Podiatric Foot &amp; Ankle Surgeon</title>
<link rel="stylesheet" href="https://fonts.googleapis.com/css2?family=Cabin:wght@400;500;600&display=swap">
<style>
  :root {
    --teal: #3f7b86;
    --teal-dark: #2f636d;
    --orange: #f26a21;
    --navy: #1f3f6e;
    --text: #3a3a3a;
    --muted: #555;
    --page: #e9e9e9;
    --panel: #ffffff;
    --line: #d6d6d6;
    --footer: #c9c9c9;
  }
  * { box-sizing: border-box; margin: 0; padding: 0; }
  html, body { width: 800px; height: 1200px; overflow: hidden; }
  body {
    position: relative;
    background: var(--page);
    font-family: "Cabin", sans-serif;
    color: var(--text);
  }
  .abs { position: absolute; }

  /* navigation */
  .main-nav {
    left: 0; top: 0; width: 800px; height: 38px;
    background: repeating-linear-gradient(90deg, var(--teal) 0 2px, var(--teal-dark) 2px 3px);
    border-bottom: 2px solid #d8d8d8;
  }
  .nav-item { top: 17px; color: #fff; font-size: 9px; font-weight: 600; }
  .nav-tab {
    top: 4px; height: 34px; background: #f4f4f4; color: #333;
    font-size: 9px; font-weight: 600; text-align: center;
  }
  .dropdown {
    background: #fff; box-shadow: 0 2px 6px rgba(0,0,0,.25);
  }
  .dropdown li {
    list-style: none; height: 24px; line-height: 24px; padding-left: 10px;
    font-size: 8.5px; color: #444; border-bottom: 1px solid #e6e6e6; position: relative;
  }
  .dropdown li:last-child { border-bottom: none; }
  .dropdown li.active { color: var(--orange); }
  .dropdown li.linked { color: var(--orange); text-decoration: underline; }
  .arrow-box {
    position: absolute; right: 6px; top: 8px; width: 7px; height: 7px; background: #ccc;
  }
  .active .arrow-box { background: var(--orange); }

  /* header */
  .brand-mark { left: 98px; top: 56px; width: 30px; height: 30px; border-radius: 50%; background: var(--navy); }
  .brand-name { left: 134px; top: 56px; font-size: 12px; font-weight: 500; color: var(--navy); }
  .brand-creds { left: 134px; top: 72px; font-size: 7px; color: var(--navy); }
  .brand-role { left: 134px; top: 82px; font-size: 7px; color: var(--navy); }
  .call-icon { left: 520px; top: 68px; width: 30px; height: 30px; border-radius: 50%; background: #fff; box-shadow: 0 1px 3px rgba(0,0,0,.2); }
  .call { left: 556px; top: 76px; font-size: 16px; color: var(--orange); }
  .call .number { color: var(--navy); margin-left: 10px; letter-spacing: 1px; }

  /* slider */
  .slider { left: 88px; top: 136px; width: 624px; height: 264px; background: var(--panel); border: 1px solid var(--line); border-radius: 3px; }
  .slide-title { left: 109px; top: 157px; font-size: 21px; color: #222; }
  .slide-text { left: 109px; top: 192px; width: 266px; font-size: 8.6px; line-height: 16px; color: var(--muted); }
  .btn-details {
    left: 182px; top: 292px; width: 79px; height: 26px; background: var(--orange);
    color: #fff; font-size: 12px; line-height: 26px; text-align: center; border: 1px solid #e0e0e0; border-radius: 2px;
  }
  .slide-photo { left: 400px; top: 148px; width: 298px; height: 197px; background: linear-gradient(90deg, #2f8a86 0%, #3d8f8a 45%, #c9c9c9 75%, #b9b9b9 100%); }
  .slide-rule { left: 107px; top: 362px; width: 586px; height: 1px; background: var(--line); }
  .dots { left: 360px; top: 377px; display: flex; gap: 4px; }
  .dots span { width: 8px; height: 8px; border-radius: 50%; background: #e4e4e4; border: 1px solid #bbb; }
  .dots span.on { background: #333; }

  /* welcome */
  .welcome-title { left: 90px; top: 460px; font-size: 24px; color: var(--orange); }
  .welcome-text { left: 90px; top: 494px; width: 310px; font-size: 11.2px; line-height: 20px; color: #333; }
  .welcome-text p + p { margin-top: 10px; }

  /* news */
  .news { left: 526px; top: 460px; width: 186px; height: 178px; background: #efefef; border: 1px solid var(--line); }
  .news-title { left: 575px; top: 469px; font-size: 15px; color: var(--orange); }
  .news-thumb { width: 36px; height: 32px; background: linear-gradient(135deg, #e8e4df, #c7b8a8); border: 1px solid #ccc; }
  .news-text { width: 134px; font-size: 8.8px; line-height: 12px; color: #555; }
  .news-text b { color: var(--navy); font-weight: 600; }
  .news-sep { left: 555px; top: 559px; width: 150px; border-top: 1px dashed #bbb; }

  /* feature cards */
  .card-photo { width: 156px; height: 101px; background: #fff; border: 1px solid #ccc; padding: 3px; }
  .card-photo div { width: 100%; height: 100%; }
  .card-title { font-size: 12px; color: var(--orange); }
  .card-text { width: 150px; font-size: 7.8px; line-height: 10.5px; color: #555; }

  /* contact */
  .contact-band { left: 0; top: 922px; width: 800px; height: 220px; background: #fafafa; }
  .contact-title { left: 182px; top: 967px; font-size: 19px; color: var(--orange); }
  .field { left: 159px; width: 146px; background: #efefef; border: 1px solid #d3d3d3; font-size: 7px; font-style: italic; color: #888; padding: 3px 8px; }
  .submit { left: 161px; top: 1086px; width: 60px; height: 16px; background: var(--orange); color: #fff; font-size: 8px; line-height: 16px; padding-left: 10px; }
  .map { left: 373px; top: 967px; width: 301px; height: 135px; background: #fff; padding: 4px; box-shadow: 0 1px 4px rgba(0,0,0,.25); }
  .map div { width: 100%; height: 100%; background: linear-gradient(135deg, #e9e4d4 0%, #c9dcae 45%, #b8d59a 70%, #e6e1cf 100%); }

  /* footer */
  .footer { left: 0; top: 1142px; width: 800px; height: 58px; background: var(--footer); }
  .copyright { left: 0; top: 1154px; width: 800px; text-align: center; font-size: 7px; color: #222; }
  .social { left: 380px; top: 1176px; display: flex; gap: 4px; }
  .social span { width: 10px; height: 10px; border-radius: 2px; background: #6b7c8c; }
</style>
</head>
<body>

<nav class="abs main-nav" aria-label="Main">
  <div class="abs nav-tab" style="left:87px;width:51px;line-height:34px;">Home</div>
  <div class="abs nav-item" style="left:151px;">Hospital Appointments</div>
  <div class="abs nav-tab" style="left:278px;top:12px;height:26px;width:81px;line-height:10px;padding-top:1px;background:#fff;">Training Programs<br>Undertaken</div>
  <div class="abs nav-item" style="left:390px;">Association Memberships</div>
  <div class="abs nav-item" style="left:529px;">Foot Conditions</div>
  <div class="abs nav-item" style="left:626px;">Referral Information</div>
</nav>

<ul class="abs dropdown" style="left:278px;top:42px;width:120px;">
  <li>Our team<span class="arrow-box"></span></li>
  <li class="active">Experience<span class="arrow-box"></span></li>
  <li>Pellentesque</li>
</ul>
<ul class="abs dropdown" style="left:398px;top:66px;width:124px;">
  <li>Lorem ipsum</li>
  <li>Dolor sit amet</li>
  <li>Nullam</li>
  <li class="linked">Bibendum</li>
</ul>

<header>
  <span class="abs brand-mark"></span>
  <div class="abs brand-name">Mr Colin Dwyer</div>
  <div class="abs brand-creds">M.Sc. B.Sc. F.A.C.P.S.</div>
  <div class="abs brand-role">Podiatric Foot &amp; Ankle Surgeon</div>
  <div class="abs call-icon">
    <svg width="30" height="30" viewBox="0 0 30 30"><path d="M10 8 l4 0 l1 5 l-2 1.5 q2 4 5 5 l1.5 -2 l5 1 l0 4 q-1 2 -3 2 q-11 -2 -13 -13 q0 -2 1.5 -3.5z" fill="#f26a21"/></svg>
  </div>
  <div class="abs call">Call Us<span class="number">08 9000 2716</span></div>
</header>

<section class="abs slider"></section>
<h1 class="abs slide-title" style="font-weight:400;">ABOUT FOOT SURGERY</h1>
<p class="abs slide-text">Etiam dignissim lectus id diam varius egestas. Curabitur vel libero massa. Phasellus scelerisque est ac enim interdum pharetra. Nam tristique venenatis tortor non interdum. Aliquam molestie sem eget ipsum dapibus congue. Cras venenatis nisi nec est faucibus consequat.</p>
<div class="abs btn-details">View Details</div>
<div class="abs slide-photo" role="img" aria-label="Photo of a surgeon examining a patient's foot"></div>
<div class="abs slide-rule"></div>
<div class="abs dots"><span class="on"></span><span></span><span></span><span></span><span></span><span></span><span></span></div>

<h2 class="abs welcome-title" style="font-weight:400;">Welcome...</h2>
<div class="abs welcome-text">
  <p>Lorem ipsum is a dummy text only. Dolor sit amet, consectetur adipiscing elit. Nullam felis mauris, eleifend ac rhoncus non, lobortis at diam. Pellentesque suscipit nulla sit amet venenatis porttitor. In augue felis.</p>
  <p>Vestibulum bibendum, nulla quis viverra pharetra, lorem dolor tincidunt turpis, ut fermentum velit ligula pretium mi. Pellentesque euismod rutrum massa.</p>
</div>

<aside class="abs news"></aside>
<svg class="abs" style="left:540px;top:465px;" width="28" height="26" viewBox="0 0 28 26"><rect x="2" y="5" width="19" height="19" fill="none" stroke="#f26a21" stroke-width="2"/><path d="M9 17 l2 -5 l12 -11 l3 3 l-12 11z" fill="#f26a21"/></svg>
<h3 class="abs news-title" style="font-weight:400;">Recent News</h3>
<div class="abs news-thumb" style="left:534px;top:510px;" role="img" aria-label="Thumbnail of a foot examination"></div>
<p class="abs news-text" style="left:577px;top:509px;">Praesent venenatis nec ligula in tincidunt. Suspendisse fringilla odio non. <b>Read more... &gt;&gt;</b></p>
<div class="abs news-sep"></div>
<div class="abs news-thumb" style="left:534px;top:575px;" role="img" aria-label="Thumbnail of a foot examination"></div>
<p class="abs news-text" style="left:577px;top:574px;">Praesent venenatis nec ligula in tincidunt. Suspendisse fringilla odio non. <b>Read more... &gt;&gt;</b></p>

<div class="abs card-photo" style="left:141px;top:709px;"><div role="img" aria-label="Photo of a gloved hand treating a foot" style="background:linear-gradient(90deg,#2a2a2a,#e4dccd 40%,#c7a466);"></div></div>
<h4 class="abs card-title" style="left:143px;top:815px;font-weight:400;">Lorem ipsum</h4>
<p class="abs card-text" style="left:144px;top:835px;">Lorem ipsum is a dummy text only. Dolor sit amet, consectetur adipiscing elit. Nullam felis mauris, eleifend ac rhoncus non.</p>

<div class="abs card-photo" style="left:322px;top:709px;"><div role="img" aria-label="Photo of a doctor testing a foot reflex" style="background:linear-gradient(90deg,#2e8a86,#7fa9a4 40%,#e6d3c2 70%,#f3f3f3);"></div></div>
<h4 class="abs card-title" style="left:325px;top:815px;font-weight:400;">Lorem ipsum</h4>
<p class="abs card-text" style="left:326px;top:835px;">Lorem ipsum is a dummy text only. Dolor sit amet, consectetur adipiscing elit. Nullam felis mauris, eleifend ac rhoncus non.</p>

<div class="abs card-photo" style="left:503px;top:709px;"><div role="img" aria-label="Photo of a foot being examined on a treatment bed" style="background:linear-gradient(90deg,#d9dde2,#e8d6c6 50%,#c9d3dc);"></div></div>
<h4 class="abs card-title" style="left:506px;top:815px;font-weight:400;">Lorem ipsum</h4>
<p class="abs card-text" style="left:507px;top:835px;">Lorem ipsum is a dummy text only. Dolor sit amet, consectetur adipiscing elit. Nullam felis mauris, eleifend ac rhoncus non.</p>

<section class="abs contact-band"></section>
<h2 class="abs contact-title" style="font-weight:400;">Contact Us</h2>
<div class="abs field" style="top:994px;height:16px;">Enter name</div>
<div class="abs field" style="top:1014px;height:16px;">Enter email address</div>
<div class="abs field" style="top:1032px;height:50px;padding-top:6px;">Your message</div>
<div class="abs submit">Submit</div>
<div class="abs map"><div role="img" aria-label="Street map showing the office location"></div></div>
<svg class="abs" style="left:508px;top:1010px;" width="24" height="30" viewBox="0 0 24 30"><path d="M12 29 C4 18 1 15 1 11 a11 11 0 0 1 22 0 c0 4 -3 7 -11 18z" fill="#f26a21"/><circle cx="12" cy="11" r="5" fill="#fff"/></svg>
<div class="abs" style="left:532px;top:1016px;height:14px;padding:0 8px;background:#333;color:#fff;font-size:7px;line-height:14px;border-radius:2px;">Our office</div>

<footer class="abs footer"></footer>
<p class="abs copyright">Copyright © 2014. YourCompanyName. All Rights Reserved</p>
<div class="abs social"><span></span><span></span><span></span></div>

</body>
</html>
```